South Florida Real Estate Brokerage Business

The name is DWELL VANTORO REAL ESTATE.
The company is a Real estate realty based in Miami.
Is targeted to Latin American clients.
Must express luxury, and efficiency.
Target clients for properties around 250k to a million +.
Vantoro means Royal in Latin.
Should communicate safety and knowledge of the product and transaction with a tech edge.

The web design needs to be a Social tool, with Chatterloop and other media integration of some sort. Needs to have a Show case place, a Search place (MLS listings) with maps and filters.
Needs to reflect luxury but also mixed with a social edge capable of engaging clients or transition them to communicate with the page.
Include the logo from the uploaded files, feel free to change the color or font per webdesign.
This is a Front en design, layout and graphics.
Possible future programming if approved.
I can receive Quotes for the Code part.

Target Market(s)

Spanish and English speakers living in Latin America and Canada looking for apartments and houses to buy.

Industry/Entity Type

Business

Requirements
Must have
• Search area.
Neighbourhood area.
Could be a blog or news area.
Client registration.
Social Plugin
Nice to have
• Social linking to networks.
Log in with chatterloop account.
Chatterloop Like.

```html
<!DOCTYPE html>
<html lang="en">
<head>
<meta charset="utf-8">
<title>Dwell Vantoro Real Estate</title>
<link rel="stylesheet" href="https://fonts.googleapis.com/css2?family=Ubuntu:wght@400;500&family=Arimo:wght@400;700&family=Open+Sans:ital@1&display=swap">
<style>
  :root {
    --page-bg: #1b1b1b;
    --page-glow: #2c2c2c;
    --header-bg: #141414;
    --tab-bg: #2a2a2a;
    --tab-border: #3a3a3a;
    --cyan: #18eef4;
    --cyan-deep: #0fa9c9;
    --yellow: #f0ea3c;
    --lime: #a8d829;
    --white: #ffffff;
    --grey-text: #9a9a9a;
    --panel-top: #2a86b9;
    --panel-bottom: #0f4f7d;
    --field-bg: #0b0b0b;
    --login-bg: #141a20;
    --rule: #3c3c3c;
    --hero-sky: #d9dbdd;
    --hero-grass: #6a8a35;
  }
  * { box-sizing: border-box; margin: 0; padding: 0; }
  html, body { width: 1163px; height: 1200px; overflow: hidden; background: var(--page-bg); }
  body { font-family: "Ubuntu", sans-serif; color: var(--white); }

  .canvas {
    position: relative; width: 1163px; height: 1200px; overflow: hidden;
    background: radial-gradient(ellipse 520px 360px at 580px 860px, var(--page-glow), var(--page-bg) 75%);
  }

  /* Header */
  .site-header { position: absolute; left: 0; top: 0; width: 1163px; height: 78px; background: var(--header-bg); }
  .brand {
    position: absolute; left: 150px; top: 22px; width: 110px;
    display: flex; align-items: center; gap: 6px;
  }
  .brand-square { width: 10px; height: 10px; background: var(--yellow); flex: none; }
  .brand-name { font-size: 11px; line-height: 13px; font-weight: 500; color: #e3d9b8; letter-spacing: .5px; }

  .main-nav { position: absolute; left: 655px; top: 0; display: flex; }
  .nav-tab {
    width: 74px; height: 78px; background: var(--tab-bg);
    border-right: 1px solid var(--tab-border);
    padding: 44px 0 0 7px; font-size: 16px; line-height: 16px; color: var(--white);
  }
  .nav-tab small { display: block; font-size: 11px; line-height: 12px; color: var(--cyan); margin-top: -13px; }
  .nav-tab.is-active {
    background: linear-gradient(#1ec4e6, #0d8fc0); color: #c8f3ff;
    padding-top: 57px; padding-left: 15px;
  }
  .nav-tab.plain { padding-top: 57px; padding-left: 8px; }
  .nav-tab.two-line { padding-top: 44px; padding-left: 8px; }
  .nav-tab.two-line small { margin-top: 0; margin-bottom: 1px; }

  /* Hero */
  .hero {
    position: absolute; left: 139px; top: 78px; width: 886px; height: 458px;
    background: linear-gradient(180deg, var(--hero-sky) 0%, #ecedee 45%, #9fae6e 62%, var(--hero-grass) 80%, #4f6c27 100%);
  }
  .hero-title {
    position: absolute; left: 83px; top: 122px; font-family: "Arimo", sans-serif;
    font-weight: 700; font-size: 33px; color: #9d9d9d; letter-spacing: .5px;
  }
  .hero-title span { color: #f29b1a; }

  /* Search bar */
  .search-bar {
    position: absolute; left: 139px; top: 536px; width: 886px; height: 170px;
    background: linear-gradient(180deg, var(--panel-top), #1a6a9c 45%, var(--panel-bottom));
    border-top: 2px solid #3ba3d4;
  }
  .search-bar > * { position: absolute; }
  .qs-title { left: 9px; top: 6px; font-size: 16px; }
  .field {
    background: var(--field-bg); border-radius: 3px; height: 22px;
    font-size: 13.5px; line-height: 22px; padding-left: 7px; color: var(--white);
    box-shadow: inset 0 0 0 1px #2a2a2a;
  }
  .divider { top: 12px; width: 1px; height: 146px; background: rgba(255,255,255,.25); }

  .listing-place { left: 230px; top: 22px; font-size: 16px; line-height: 20px; color: var(--yellow); }
  .show-only { left: 230px; top: 67px; font-size: 11px; color: var(--yellow); font-weight: 500; }
  .filter-list { left: 239px; top: 84px; list-style: none; font-size: 11.5px; line-height: 12px; }
  .filter-list li { position: relative; padding-left: 20px; margin-bottom: 3px; }
  .filter-list li::before {
    content: ""; position: absolute; left: 0; top: 1px; width: 10px; height: 10px;
    background: #fff; border: 1px solid #333;
  }
  .pill-button {
    height: 21px; border-radius: 11px; background: linear-gradient(#f4f4f4, #bcbcbc);
    color: #444; font-size: 12px; line-height: 21px; text-align: center;
  }
  .map-area {
    left: 378px; top: 9px; width: 204px; height: 124px;
    background: linear-gradient(135deg, #b9cde8, #d7dfc9 45%, #c9d6e6);
    border: 2px solid #8aa9c2;
  }

  .login-box {
    left: 602px; top: 9px; width: 277px; height: 154px; border-radius: 8px;
    background: var(--login-bg); box-shadow: inset 0 0 0 1px #2c3640;
  }
  .login-box > * { position: absolute; }
  .login-title { left: 16px; top: 4px; font-family: "Arimo", sans-serif; font-size: 16px; }
  .field-label { left: 16px; font-family: "Arimo", sans-serif; font-size: 7px; }
  .login-input {
    left: 17px; width: 112px; height: 18px; border-radius: 4px;
    background: linear-gradient(#fff, #dcdcdc); color: #aaa; font-size: 7px; line-height: 18px; text-align: center;
  }
  .small-button {
    height: 19px; border-radius: 9px; background: linear-gradient(#cfcfcf, #8d8d8d);
    color: #333; font-family: "Arimo", sans-serif; font-size: 12px; line-height: 19px; text-align: center;
  }
  .social-login {
    left: 16px; top: 127px; width: 113px; height: 19px; background: #3b5591; border-radius: 2px;
    display: flex; align-items: center; gap: 6px; padding-left: 4px;
    font-family: "Arimo", sans-serif; font-size: 8px;
  }
  .social-login i { width: 11px; height: 11px; background: #fff; display: block; }
  .login-split { left: 153px; top: 8px; width: 1px; height: 138px; background: #2e3a44; }
  .signup-title { left: 163px; top: 4px; font-family: "Arimo", sans-serif; font-size: 16px; color: var(--yellow); }
  .signup-lead { left: 163px; top: 20px; font-family: "Arimo", sans-serif; font-size: 12px; line-height: 12px; color: var(--cyan); }
  .signup-note { left: 163px; top: 48px; width: 104px; font-family: "Arimo", sans-serif; font-size: 6.5px; line-height: 7.5px; }
  .contact-line { left: 163px; top: 126px; font-family: "Arimo", sans-serif; font-size: 12px; line-height: 12px; }
  .contact-line em { color: var(--lime); display: block; }
  .contact-line b { color: var(--yellow); font-weight: 400; }

  /* Intro */
  .intro-heading { position: absolute; left: 148px; top: 740px; font-family: "Arimo", sans-serif; color: var(--cyan); }
  .intro-heading strong { font-size: 50px; font-weight: 400; }
  .intro-heading span { font-size: 18px; margin-left: 8px; }

  .brand-seal {
    position: absolute; left: 150px; top: 819px; width: 199px; height: 199px; border-radius: 50%;
    background: radial-gradient(circle at 45% 35%, #2b2b2b, #151515 70%);
    box-shadow: 0 0 0 3px #1a1a1a, 0 6px 14px rgba(0,0,0,.6);
    display: flex; align-items: center; justify-content: center; text-align: center;
  }
  .brand-seal p { font-size: 17px; line-height: 20px; color: #6d6d6d; font-weight: 500; }

  .intro-copy { position: absolute; left: 368px; top: 807px; width: 648px; font-family: "Arimo", sans-serif; }
  .intro-lead { font-size: 16.5px; line-height: 17px; text-align: justify; margin-bottom: 16px; }
  .intro-lead mark { background: none; color: var(--yellow); }
  .intro-rule { height: 1px; background: var(--rule); margin: 20px 0 20px; }
  .intro-detail { font-family: "Open Sans", sans-serif; font-style: italic; font-size: 12.3px; line-height: 16.5px; margin-bottom: 17px; }

  /* Footer */
  .site-footer { position: absolute; left: 148px; top: 1083px; width: 868px; border-top: 1px solid var(--rule); font-family: "Arimo", sans-serif; color: var(--grey-text); font-weight: 700; }
  .footer-links { display: flex; gap: 11px; font-size: 7.5px; margin-top: 22px; }
  .legal { font-size: 7.3px; line-height: 11.2px; margin-top: 15px; }
</style>
</head>
<body>
<div class="canvas">

  <header class="site-header">
    <div class="brand">
      <span class="brand-square"></span>
      <span class="brand-name">DWELL VANTORO REAL ESTATE</span>
    </div>
    <nav class="main-nav">
      <div class="nav-tab is-active">Home</div>
      <div class="nav-tab two-line"><small>Search for</small>Home</div>
      <div class="nav-tab two-line"><small>Our</small>Services</div>
      <div class="nav-tab plain">About</div>
      <div class="nav-tab plain">Contact</div>
    </nav>
  </header>

  <section class="hero" role="img" aria-label="Photograph of a couple standing on a green lawn in front of a modern white house">
    <h1 class="hero-title">WELCOME<span>.</span></h1>
  </section>

  <section class="search-bar">
    <h2 class="qs-title">MLS Quick Search</h2>
    <div class="field" style="left:9px;top:29px;width:202px">Type an Address, Area or MLS#</div>
    <div class="field" style="left:9px;top:57px;width:202px">Property Type</div>
    <div class="field" style="left:9px;top:84px;width:89px">Min Price</div>
    <div class="field" style="left:122px;top:84px;width:89px">Max Price</div>
    <div class="field" style="left:9px;top:113px;width:89px">Beds</div>
    <div class="field" style="left:122px;top:113px;width:89px">Baths</div>
    <div class="field" style="left:9px;top:142px;width:89px">SqFt</div>
    <div class="field" style="left:122px;top:142px;width:89px">Acres</div>

    <div class="divider" style="left:220px"></div>

    <p class="listing-place">Florida :<br>2,345 Listings</p>
    <p class="show-only">SHOW ONLY</p>
    <ul class="filter-list">
      <li>Foreclosure /<br>Bank-owned</li>
      <li>Short Sale Listings</li>
      <li>HUD Owned</li>
    </ul>
    <div class="pill-button" style="left:230px;top:139px;width:129px">Search</div>

    <div class="divider" style="left:368px"></div>

    <div class="map-area" role="img" aria-label="Map of Florida showing listing locations"></div>
    <div class="pill-button" style="left:378px;top:139px;width:204px">Show Full Map &amp; Directions</div>

    <div class="login-box">
      <p class="login-title">login.</p>
      <p class="field-label" style="top:25px">email:</p>
      <div class="login-input" style="top:34px">Name</div>
      <p class="field-label" style="top:58px">password:</p>
      <div class="login-input" style="top:68px">●●●●●●●●●</div>
      <div class="small-button" style="left:73px;top:96px;width:56px">login</div>
      <div class="social-login"><i></i>Sign in with Chatterloop</div>

      <div class="login-split"></div>
      <p class="signup-title">Sign up?</p>
      <p class="signup-lead">Lorem ipsum<br>dolor sit amet,</p>
      <p class="signup-note">consectetur adipiscing elit. Praesent sapien nulla, varius eu viverra nisi. Proin imperdiet lacinia massa id feugiat.</p>
      <div class="small-button" style="left:163px;top:95px;width:56px">signup</div>
      <p class="contact-line"><em>Get in touch</em><b>XXX-XXXXXX</b></p>
    </div>
  </section>

  <h2 class="intro-heading"><strong>Welcome</strong><span>to our real estate sites</span></h2>

  <div class="brand-seal"><p>DWELL VANTORO<br>REAL ESTATE</p></div>

  <article class="intro-copy">
    <p class="intro-lead">.Lorem ipsum dolor sit amet, consectetur adipiscing elit. Vivamus id purus nunc, ut <mark>hendrerit</mark> arcu. <mark>Praesent ut mauris</mark> mi.</p>
    <p class="intro-lead">.Lorem ipsum dolor sit amet, consectetur adipiscing elit. Vivamus id purus nunc, ut <mark>hendrerit</mark> arcu.</p>
    <div class="intro-rule"></div>
    <p class="intro-detail">Lorem ipsum dolor sit amet, consectetur adipiscing elit. Vivamus id purus nunc, ut hendrerit arcu. Praesent ut mauris mi. Sed ut lacus nulla, sed pharetra ligula. Nullam dictum iaculis diam, vel tempus neque pellentesque et. Integer aliquet commodo nunc sit amet aliquet. Pellentesque eu turpis dolor.</p>
    <p class="intro-detail">Lorem ipsum dolor sit amet, consectetur adipiscing elit. Vivamus id purus nunc, ut hendrerit arcu. Praesent ut mauris mi. Sed ut lacus nulla, sed pharetra ligula. Nullam dictum iaculis diam, vel tempus neque pellentesque et. Integer aliquet commodo nunc sit amet aliquet. Pellentesque eu turpis dolor.</p>
  </article>

  <footer class="site-footer">
    <nav class="footer-links">
      <span>© 2012</span><span>TERMS OF USE</span><span>PRIVACY POLICY</span><span>ADDITIONAL RESOURCES</span>
    </nav>
    <p class="legal">THE PROPERTY LISTING DATA AND INFORMATION SET FORTH HEREIN WERE PROVIDED TO LISTING EXCHANGE NETWORK, INC. FROM THIRD PARTY SOURCES, INCLUDING SELLERS, LESSORS AND PUBLIC RECORDS, AND WERE COMPILED BY LISTING EXCHANGE NETWORK, INC. THE PROPERTY LISTING DATA AND INFORMATION ARE FOR THE PERSONAL, NON COMMERCIAL USE OF CONSUMERS HAVING A GOOD FAITH INTEREST IN PURCHASING OR LEASING LISTED PROPERTIES OF THE TYPE DISPLAYED TO THEM AND MAY NOT BE USED FOR ANY PURPOSE OTHER THAN TO IDENTIFY PROSPECTIVE PROPERTIES WHICH SUCH CONSUMERS MAY HAVE A GOOD FAITH INTEREST IN PURCHASING OR LEASING. LISTING EXCHANGE NETWORK, INC. AND ITS SUBSCRIBERS DISCLAIM ANY AND ALL REPRESENTATIONS AND WARRANTIES AS TO THE ACCURACY OF THE PROPERTY LISTING DATA AND INFORMATION SET FORTH HEREIN.</p>
  </footer>

</div>
</body>
</html>
```